Oakhaven Construction Need an information and interactive website with client portal. We have ou

Need to have a client log in screen for work orders and estimate requests.
Nice informational landing page.

Oakhaven is a full service general contractor servicing apartment complexes;
maintenance of grounds and apartments - remodeling and construction.

Design Specifics: We are pretty open here. Some good examples are
www.marrowpeakbuilders.com , tovelresidence.com and www.quillbyworksite.com

For the site we need:
Homepage - to explain services
Roofing page
Apartment Page
Client Portal - where clients can set up accounts to set up work/estimate request that will be routed to our email

--Will need coding, plan to host site on Wordpress

Target Market(s)

Multi family, Residential and commercial clients

Industry/Entity Type

Construction

Coding

Coded - Design and coding required

Number of Pages Required

3 page

Font styles to use
Serif

Requirements
Must have
• Client portal
Nice to have
• Not sure. please advise

```html
<!DOCTYPE html>
<html lang="en">
<head>
<meta charset="utf-8">
<title>Oakhaven Construction</title>
<link href="https://fonts.googleapis.com/css2?family=Roboto:wght@300;400;500;700&display=swap" rel="stylesheet">
<style>
:root{
  --red:#b51215;
  --dark:#231f1e;
  --panel:#3a3532;
  --ink:#111111;
  --muted:#7a7a7a;
  --line:#444;
  --field:#5a5552;
  --white:#ffffff;
  --faint:#f3f3f3;
}
*{box-sizing:border-box;margin:0;padding:0}
html,body{width:1200px;height:2671px;overflow:hidden;background:var(--white)}
body{position:relative;font-family:"Roboto",Arial,sans-serif;color:var(--ink)}
.abs{position:absolute}
a{color:inherit;text-decoration:none}

/* header */
.site-header{position:absolute;left:0;top:0;width:1200px;height:84px;background:var(--white)}
.brand{position:absolute;display:flex;align-items:center;gap:8px;font-weight:700;color:var(--ink)}
.brand-mark{width:14px;height:14px;background:var(--red)}
.site-header .brand{left:155px;top:28px;font-size:22px}
.main-nav{position:absolute;left:360px;top:26px;display:flex;gap:8px;font-size:12px;font-weight:500}
.main-nav a{display:block;padding:9px 18px;height:32px}
.main-nav a.active{background:var(--red);color:var(--white);clip-path:polygon(6% 0,100% 0,94% 100%,0 100%)}
.login-btn{position:absolute;left:935px;top:26px;width:108px;height:32px;background:var(--red);color:var(--white);font-size:11px;display:flex;align-items:center;justify-content:center}

/* hero */
.hero{position:absolute;left:0;top:84px;width:1200px;height:400px}
.hero-photo{position:absolute;inset:0;background:linear-gradient(180deg,#5b5e66 0%,#4a4a4e 45%,#3b3230 80%,#2b2522 100%)}
.hero-title{position:absolute;left:155px;top:104px;font-size:32px;font-weight:500;color:var(--white)}
.hero-sub{position:absolute;left:155px;top:158px;font-size:19px;font-weight:300;line-height:33px;color:#e8e8e8;width:400px}
.btn-slant{position:absolute;background:var(--red);color:var(--white);display:flex;align-items:center;justify-content:center;clip-path:polygon(8% 0,100% 0,92% 100%,0 100%)}
.hero .btn-slant{left:140px;top:249px;width:162px;height:41px;font-size:12px}

/* faint section words */
.ghost{position:absolute;font-size:72px;font-weight:700;color:var(--faint);white-space:nowrap}
.ghost.vertical{transform:rotate(-90deg);transform-origin:left top}

/* about */
.about-box{position:absolute;left:155px;top:534px;width:532px;height:356px;border:4px solid var(--ink);padding:44px 24px}
.about-box .brand{position:static;font-size:15px;margin-bottom:34px}
.about-title{font-size:18px;font-weight:500;margin-bottom:16px}
.about-title span,.red{color:var(--red)}
.about-text{font-size:11.5px;line-height:18px;color:var(--muted);width:310px}
.read-more{display:inline-block;font-size:11px;font-weight:500;color:var(--red);border-bottom:1px solid var(--red);margin-top:24px}
.about-frame{position:absolute;left:513px;top:577px;width:380px;height:60px;border-top:2px solid var(--ink);border-right:2px solid var(--ink)}
.about-photo{position:absolute;left:513px;top:618px;width:530px;height:313px;background:linear-gradient(160deg,#a9c0d6 0%,#5c7f9e 45%,#24384c 100%)}

/* section headings */
.heading{position:absolute;display:flex;align-items:center;font-size:18px;font-weight:500}
.heading .rule{width:72px;height:2px;background:#888}
.heading .label{padding:12px 18px;border-left:2px solid #888;border-right:2px solid #888}

/* services */
.service{position:absolute;width:270px}
.hex{display:block;margin-bottom:24px}
.service h3{font-size:15px;font-weight:500;margin-bottom:16px}
.service h3.red{color:var(--red)}
.service p{font-size:11.5px;line-height:18px;color:var(--muted)}
.service .read-more{margin-top:30px}

/* feature cards */
.card-frame{position:absolute;width:282px;height:180px;border-top:3px solid var(--ink);border-left:3px solid var(--ink);border-right:3px solid var(--ink)}
.card-photo{position:absolute;width:400px;height:283px}
.card-bar{position:absolute;width:400px;height:39px;display:flex;justify-content:space-between;align-items:center;padding:0 14px;color:var(--white);font-size:15px;font-weight:500}
.card-bar small{font-size:11px;border-bottom:1px solid var(--white)}
.bar-red{background:var(--red)}
.bar-dark{background:var(--dark)}

/* estimate */
.estimate-photo{position:absolute;left:0;top:1803px;width:513px;height:369px;background:linear-gradient(200deg,#2f6fb7 0%,#6fa3d8 50%,#c8d4df 100%)}
.estimate-panel{position:absolute;left:513px;top:1803px;width:687px;height:369px;background:linear-gradient(180deg,#3d3633,#2e2926)}
.estimate-panel .heading{left:74px;top:32px;color:var(--white)}
.estimate-panel .heading .rule{width:72px;background:#aaa}
.estimate-panel .heading .label{border-color:#aaa}
.field{position:absolute;background:var(--field);color:#c8c8c8;font-size:10px;padding:9px 8px}
.estimate-panel .btn-slant{left:74px;top:289px;width:100px;height:30px;font-size:11px}

/* newsletter */
.newsletter{position:absolute;left:0;top:2172px;width:1200px;height:103px;background:var(--dark)}
.newsletter-red{position:absolute;left:0;top:0;width:587px;height:103px;background:var(--red);clip-path:polygon(0 0,100% 0,94% 100%,0 100%)}
.newsletter h4{position:absolute;left:155px;top:27px;color:var(--white);font-size:17px;font-weight:500}
.newsletter p{position:absolute;left:155px;top:53px;color:#f2d6d6;font-size:11px}
.news-input{position:absolute;left:612px;top:40px;width:430px;height:38px;border-bottom:1px solid #bbb;color:#bbb;font-size:11px;padding-top:14px}
.news-btn{position:absolute;left:877px;top:40px;width:166px;height:38px;border:1px solid #ccc;color:var(--white);font-size:12px;display:flex;align-items:center;justify-content:center;clip-path:polygon(5% 0,100% 0,95% 100%,0 100%)}

/* contact */
.contact-item{position:absolute;display:flex;align-items:center;gap:18px;top:2412px}
.contact-item .txt{font-size:11.5px;line-height:18px;color:var(--muted)}
.contact-item .big{font-size:22px;color:var(--red);font-weight:300}
.contact-item .mail{color:var(--red);text-decoration:underline;font-size:12px}

/* footer */
.site-footer .brand{left:155px;top:2530px;font-size:22px}
.footer-nav{position:absolute;left:364px;top:2534px;font-size:11.5px;font-weight:500;display:flex;gap:14px}
.footer-nav .sep{color:var(--ink);font-weight:400}
.social{position:absolute;left:918px;top:2529px;display:flex;gap:6px}
.social span{width:27px;height:27px;border-radius:50%;background:var(--ink)}
.social span.alt{background:var(--red)}
.copyright{position:absolute;left:0;top:2622px;width:1200px;height:49px;background:var(--red);color:var(--white);font-size:11.5px;padding:19px 0 0 155px}
.to-top{position:absolute;left:1025px;top:2638px;width:18px;height:18px;border-radius:50%;background:var(--white)}
</style>
</head>
<body>

<header class="site-header">
  <div class="brand"><span class="brand-mark"></span>Oakhaven</div>
  <nav class="main-nav">
    <a class="active" href="#">Home</a>
    <a href="#">About Us</a>
    <a href="#">Services</a>
    <a href="#">Maintenance</a>
    <a href="#">Remodeling</a>
    <a href="#">Contact Us</a>
  </nav>
  <a class="login-btn" href="#">Login &amp; Register</a>
</header>

<section class="hero">
  <div class="hero-photo" role="img" aria-label="City skyline with high-rise towers under a cloudy sky, darkened"></div>
  <h1 class="hero-title">Oakhaven Construction</h1>
  <p class="hero-sub">is a full service general contractor servicing apartment complexes</p>
  <a class="btn-slant" href="#">Explore More</a>
</section>

<div class="ghost vertical" style="left:48px;top:795px">About Us</div>
<section class="about">
  <div class="about-frame"></div>
  <div class="about-box">
    <div class="brand"><span class="brand-mark"></span>Oakhaven</div>
    <h2 class="about-title">Welcome To <span>Oakhaven</span></h2>
    <p class="about-text">There are many variations of passages of Lorem Ipsum available, but the majority have suffered alteration in some form, by injected humour, or randomised words which don't look even slightly believable. If you are going to use a passage of Lorem Ipsum, you need to be sure there isn't anything embarrassing hidden in the middle of text. All the Lorem Ipsum generators</p>
    <a class="read-more" href="#">Read More &raquo;</a>
  </div>
  <div class="about-photo" role="img" aria-label="Glass office towers seen from below against a blue sky"></div>
</section>

<div class="ghost" style="left:52px;top:966px">Services</div>
<div class="heading" style="left:155px;top:980px"><span class="rule"></span><span class="label">Our <span class="red">Services</span></span><span class="rule"></span></div>

<section class="services">
  <div class="service" style="left:155px;top:1066px">
    <svg class="hex" width="135" height="120" viewBox="0 0 135 120">
      <polygon points="38,4 98,4 130,60 98,116 38,116 8,60" fill="#e0e0e0"/>
      <polygon points="30,2 88,2 118,58 88,114 30,114 0,58" fill="#111"/>
      <g stroke="#fff" stroke-width="3" fill="none"><circle cx="50" cy="52" r="12"/><circle cx="76" cy="62" r="9"/><line x1="40" y1="80" x2="86" y2="80"/></g>
    </svg>
    <h3>Maintenance</h3>
    <p>Sed ut perspiciatis unde omnis iste natus error sit voluptatem accusantium doloremque laudantium, totam rem aperiam, eaque...</p>
    <a class="read-more" href="#">Read More &raquo;</a>
  </div>
  <div class="service" style="left:459px;top:1066px">
    <svg class="hex" width="135" height="120" viewBox="0 0 135 120">
      <polygon points="38,4 98,4 130,60 98,116 38,116 8,60" fill="#e0e0e0"/>
      <polygon points="30,2 88,2 118,58 88,114 30,114 0,58" fill="#b51215"/>
      <g stroke="#fff" stroke-width="4" stroke-linecap="round"><line x1="42" y1="40" x2="76" y2="76"/><line x1="76" y1="40" x2="42" y2="76"/></g>
    </svg>
    <h3 class="red">Remodeling</h3>
    <p>Sed ut perspiciatis unde omnis iste natus error sit voluptatem accusantium doloremque laudantium, totam rem aperiam, eaque...</p>
    <a class="read-more" href="#">Read More &raquo;</a>
  </div>
  <div class="service" style="left:764px;top:1066px">
    <svg class="hex" width="135" height="120" viewBox="0 0 135 120">
      <polygon points="38,4 98,4 130,60 98,116 38,116 8,60" fill="#e0e0e0"/>
      <polygon points="30,2 88,2 118,58 88,114 30,114 0,58" fill="#111"/>
      <g stroke="#fff" stroke-width="3" fill="none"><rect x="44" y="38" width="16" height="40"/><rect x="60" y="30" width="16" height="48"/><line x1="38" y1="78" x2="82" y2="78"/></g>
    </svg>
    <h3>General Construction</h3>
    <p>Sed ut perspiciatis unde omnis iste natus error sit voluptatem accusantium doloremque laudantium, totam rem aperiam, eaque...</p>
    <a class="read-more" href="#">Read More &raquo;</a>
  </div>
</section>

<section class="features">
  <div class="card-frame" style="left:155px;top:1383px"></div>
  <div class="card-photo" style="left:187px;top:1415px;background:linear-gradient(160deg,#6e8080 0%,#5a3a30 55%,#7a2e22 100%)" role="img" aria-label="Steep red tiled roof of a house against a misty sky"></div>
  <div class="card-bar bar-red" style="left:187px;top:1716px">Roofings<small>More Info &raquo;</small></div>

  <div class="card-frame" style="left:612px;top:1383px"></div>
  <div class="card-photo" style="left:644px;top:1415px;background:linear-gradient(170deg,#3c86c8 0%,#9cc2e0 45%,#d8d8d4 100%)" role="img" aria-label="Modern white apartment building with staggered balconies"></div>
  <div class="card-bar bar-dark" style="left:644px;top:1716px">Appartments<small>More Info &raquo;</small></div>
</section>

<section class="estimate">
  <div class="estimate-photo" role="img" aria-label="Tall white residential tower with balconies under a blue sky"></div>
  <div class="estimate-panel">
    <div class="heading"><span class="rule"></span><span class="label">Get Free Estimation</span><span class="rule"></span></div>
    <div class="field" style="left:74px;top:112px;width:216px;height:31px">Name :</div>
    <div class="field" style="left:315px;top:112px;width:215px;height:31px">Email :</div>
    <div class="field" style="left:74px;top:160px;width:216px;height:31px">Phone :</div>
    <div class="field" style="left:315px;top:160px;width:215px;height:31px">Address :</div>
    <div class="field" style="left:74px;top:208px;width:456px;height:54px">Message :</div>
    <a class="btn-slant" href="#">Submit</a>
  </div>
</section>

<section class="newsletter">
  <div class="newsletter-red"></div>
  <h4>Get our Daily News and Offers</h4>
  <p>On the other hand, we denounce with righteous indignation.</p>
  <div class="news-input">Enter Your Email...</div>
  <a class="news-btn" href="#">Subscribe Now!</a>
</section>

<div class="ghost" style="left:52px;top:2306px">Contact Us</div>
<div class="heading" style="left:155px;top:2322px"><span class="rule"></span><span class="label">Contact <span class="red">Us</span></span><span class="rule"></span></div>

<section class="contact">
  <div class="contact-item" style="left:155px">
    <svg width="76" height="66" viewBox="0 0 76 66"><polygon points="20,3 56,3 74,33 56,63 20,63 2,33" fill="#ddd"/><polygon points="16,0 50,0 68,32 50,64 16,64 0,32" fill="#111"/><path d="M34 20a9 9 0 0 1 9 9c0 7-9 16-9 16s-9-9-9-16a9 9 0 0 1 9-9z" fill="none" stroke="#fff" stroke-width="2"/><circle cx="34" cy="29" r="3" fill="#fff"/></svg>
    <div class="txt">272 Lorem Avenue<br>Lorem Park, FL 12345</div>
  </div>
  <div class="contact-item" style="left:459px">
    <svg width="76" height="66" viewBox="0 0 76 66"><polygon points="20,3 56,3 74,33 56,63 20,63 2,33" fill="#ddd"/><polygon points="16,0 50,0 68,32 50,64 16,64 0,32" fill="#111"/><path d="M26 22l5-3 4 8-3 2c1 3 4 6 7 7l2-3 8 4-3 5c-10 0-20-10-20-20z" fill="#fff"/></svg>
    <div class="txt">Phone :<br><span class="big">+123-456-7890</span></div>
  </div>
  <div class="contact-item" style="left:764px">
    <svg width="76" height="66" viewBox="0 0 76 66"><polygon points="20,3 56,3 74,33 56,63 20,63 2,33" fill="#ddd"/><polygon points="16,0 50,0 68,32 50,64 16,64 0,32" fill="#111"/><g fill="none" stroke="#fff" stroke-width="2"><rect x="22" y="22" width="24" height="18"/><polyline points="22,22 34,32 46,22"/></g></svg>
    <div class="txt">Email :<br><span class="mail">info@oakhavenconstruction.com</span></div>
  </div>
</section>

<footer class="site-footer">
  <div class="brand"><span class="brand-mark"></span>Oakhaven</div>
  <nav class="footer-nav">
    <a class="red" href="#">Home</a><span class="sep">/</span>
    <a href="#">About Us</a><span class="sep">/</span>
    <a href="#">Services</a><span class="sep">/</span>
    <a href="#">Maintenance</a><span class="sep">/</span>
    <a href="#">Remodeling</a><span class="sep">/</span>
    <a href="#">Contact Us</a>
  </nav>
  <div class="social"><span></span><span class="alt"></span><span></span><span></span></div>
  <div class="copyright">Copyright &copy; 2016 Oakhaven Construction. &nbsp;&nbsp;All rights reserved</div>
  <div class="to-top"></div>
</footer>

</body>
</html>
```